Corporate Design für Hausverwalterin und Immobilienvermarktung
Zielgruppe
Hausverwalterin und Immobilienvermarktung
Aufgabenstellung
wir sind im Immobiliensektor unterwegs und das Design soll edel und hochwertig sein

```html
<!DOCTYPE html>
<html lang="de">
<head>
<meta charset="utf-8">
<title>Marlen Immobilien – Geschäftsausstattung</title>
<link href="https://fonts.googleapis.com/css2?family=Montserrat:wght@400;500;700&display=swap" rel="stylesheet">
<style>
  :root {
    --navy: #173044;
    --gold: #d0b068;
    --sand: #eadcb9;
    --paper: #ffffff;
    --stage: #ffffff;
    --ink: #1d1d1d;
  }
  * { box-sizing: border-box; margin: 0; padding: 0; }
  html, body { width: 849px; height: 1200px; overflow: hidden; background: var(--stage); }
  body { position: relative; font-family: "Montserrat", sans-serif; }

  .card { position: absolute; top: 43px; width: 343px; height: 223px; background: var(--navy); color: var(--paper); }
  .card--front { left: 74px; }
  .card--back { left: 432px; }

  .brand-mark { display: flex; align-items: center; gap: 7px; color: var(--gold); font-weight: 500; white-space: nowrap; }
  .brand-mark__dot { width: 9px; height: 9px; border-radius: 50%; background: var(--gold); flex: none; }
  .brand-tagline { color: var(--gold); font-size: 7px; letter-spacing: 0.9px; text-transform: uppercase; }

  .card--front .brand { position: absolute; left: 0; right: 0; top: 90px; display: flex; flex-direction: column; align-items: center; gap: 6px; }
  .card--front .brand-mark { font-size: 19px; }

  .card--back .intro { position: absolute; left: 29px; top: 16px; width: 145px; }
  .rule { width: 102px; height: 2px; background: var(--paper); margin-bottom: 5px; }
  .intro__title { font-size: 9px; font-weight: 700; line-height: 1.3; text-transform: uppercase; }
  .intro__text { margin-top: 4px; font-size: 5.2px; line-height: 1.55; text-transform: uppercase; }
  .services { position: absolute; left: 29px; top: 123px; list-style: none; }
  .services li { margin-bottom: 2px; }
  .service__label { display: inline-block; background: var(--paper); color: var(--navy); font-size: 7.5px; font-weight: 700; padding: 0 2px; line-height: 1.25; }
  .service__text { display: block; font-size: 8px; line-height: 1.3; }

  .card--back .brand-mark { position: absolute; left: 222px; top: 70px; font-size: 14px; }
  .card--back .contact { position: absolute; left: 197px; top: 143px; }
  .contact .rule { width: 100px; margin-bottom: 3px; }
  .contact__name { font-size: 7.5px; font-weight: 700; }
  .contact__claim { font-size: 7.5px; margin-bottom: 6px; }
  .contact__list { list-style: none; }
  .contact__list li { display: flex; align-items: center; gap: 4px; font-size: 7.5px; line-height: 1.9; }
  .icon { width: 11px; height: 11px; flex: none; }

  .letterhead { position: absolute; left: 114px; top: 285px; width: 621px; height: 876px; background: var(--paper); overflow: hidden; box-shadow: 0 0 0 1px #eeeeee; }
  .letterhead .brand { position: absolute; left: 72px; top: 80px; display: flex; flex-direction: column; align-items: center; gap: 6px; }
  .letterhead .brand-mark { font-size: 16px; }
  .letterhead .brand-tagline { font-size: 6px; }
  .letterhead .contact { position: absolute; left: 416px; top: 47px; color: var(--ink); }
  .letterhead .contact__name { font-size: 9.5px; }
  .letterhead .contact__claim { font-size: 9.5px; margin-bottom: 5px; }
  .letterhead .contact__list li { font-size: 10px; line-height: 1.85; gap: 5px; margin-left: 4px; }
  .letterhead .icon { width: 13px; height: 13px; }

  .watermark { position: absolute; left: 28px; bottom: 60px; color: var(--sand); font-size: 150px; font-weight: 700; line-height: 1; letter-spacing: -4px; }
  .watermark-band { position: absolute; left: 0; bottom: 0; width: 400px; height: 60px; background: var(--sand); border-top-right-radius: 60px 40px; }
</style>
</head>
<body>

<section class="card card--front" aria-label="Visitenkarte Vorderseite">
  <div class="brand">
    <div class="brand-mark"><span class="brand-mark__dot"></span>Marlen Immobilien</div>
    <div class="brand-tagline">Verwaltung und Vermarktung</div>
  </div>
</section>

<section class="card card--back" aria-label="Visitenkarte Rückseite">
  <div class="intro">
    <div class="rule"></div>
    <h2 class="intro__title">Ganzheitliche Immobilienbetreuung mit Strategie.</h2>
    <p class="intro__text">Als zertifizierte Hausverwalterin &amp; Immobilienmaklerin gemäß §34c GewO verbinde ich klassische Verwaltung mit wertoptimierter Vermarktung</p>
  </div>
  <ul class="services">
    <li><span class="service__label">HAUSVERWALTUNG</span><span class="service__text">Rechtssicher &amp; Entlastend</span></li>
    <li><span class="service__label">ASSET MANAGEMENT</span><span class="service__text">Strategische Ertragssteigerung</span></li>
    <li><span class="service__label">VERKAUF</span><span class="service__text">Marktgerecht &amp; Professionell</span></li>
  </ul>
  <div class="brand-mark"><span class="brand-mark__dot"></span>Marlen</div>
  <div class="contact">
    <div class="rule"></div>
    <p class="contact__name">Marlen Immobilien</p>
    <p class="contact__claim">Ihr Eigentum in zuverlässigen Händen.</p>
    <ul class="contact__list">
      <li><svg class="icon" viewBox="0 0 24 24" fill="none" stroke="currentColor" stroke-width="2"><path d="M5 3h4l2 5-3 2a12 12 0 0 0 6 6l2-3 5 2v4a2 2 0 0 1-2 2A17 17 0 0 1 3 5a2 2 0 0 1 2-2z"/></svg>0151 600 12 34</li>
      <li><svg class="icon" viewBox="0 0 24 24" fill="none" stroke="currentColor" stroke-width="2"><rect x="3" y="5" width="18" height="14" rx="1"/><path d="M3 6l9 7 9-7"/></svg>info@marlen-immobilien.de</li>
      <li><svg class="icon" viewBox="0 0 24 24" fill="none" stroke="currentColor" stroke-width="2"><circle cx="12" cy="12" r="9"/><path d="M3 12h18M12 3c3 3 3 15 0 18M12 3c-3 3-3 15 0 18"/></svg>www.marlen-immobilien.de</li>
    </ul>
  </div>
</section>

<section class="letterhead" aria-label="Briefbogen">
  <div class="brand">
    <div class="brand-mark"><span class="brand-mark__dot"></span>Marlen Immobilien</div>
    <div class="brand-tagline">Verwaltung und Vermarktung</div>
  </div>
  <div class="contact">
    <p class="contact__name">Marlen Immobilien</p>
    <p class="contact__claim">Ihr Eigentum in zuverlässigen Händen.</p>
    <ul class="contact__list">
      <li><svg class="icon" viewBox="0 0 24 24" fill="none" stroke="currentColor" stroke-width="2"><path d="M5 3h4l2 5-3 2a12 12 0 0 0 6 6l2-3 5 2v4a2 2 0 0 1-2 2A17 17 0 0 1 3 5a2 2 0 0 1 2-2z"/></svg>0151 600 12 34</li>
      <li><svg class="icon" viewBox="0 0 24 24" fill="none" stroke="currentColor" stroke-width="2"><rect x="3" y="5" width="18" height="14" rx="1"/><path d="M3 6l9 7 9-7"/></svg>info@marlen-immobilien.de</li>
      <li><svg class="icon" viewBox="0 0 24 24" fill="none" stroke="currentColor" stroke-width="2"><circle cx="12" cy="12" r="9"/><path d="M3 12h18M12 3c3 3 3 15 0 18M12 3c-3 3-3 15 0 18"/></svg>www.marlen-immobilien.de</li>
    </ul>
  </div>
  <div class="watermark" aria-hidden="true">Marlen</div>
  <div class="watermark-band" aria-hidden="true"></div>
</section>

</body>
</html>
```